New Homepage for young Boston startup

We want a new website design for our company. We need you to design the homepage for it. If your design is chosen we may ask you also to design the website template page that is used for all secondary pages, Blog template page & Email template for email newsletter.

end deliverable in this stage is homepage only in both PSD/AI and JPG. Please see the attached document for detailed requirements of the job to be done.

the attachment contains a suggested wireframe (if you feel things are missing or things are redundant feel free to add them or leave them out of the design. Please also have a look at our existing homepage (www.tutorbrix.com), although we love to have a fresher design.

Examples of websites we very much like:
http://www.mulo.vq/
www.fitrund.com
https://vobe.com

Made a small mistake in the link to a website that I really like. It should have been: http://www.mulo.vq/

instead of mulovq.com which is horrible :)

Reason: I've extended the deadline to give some of you more time to finish your work.

Target Market(s)

We build a mobile solution for studying the KVEX test. Our target audience are College educated people 20-35 years old, interested in studying for the KVEX as they need to apply for a school that requires the KVEX (most international MBA's do).

Industry/Entity Type

It Company

Requirements
Must have
• complete homepage design with the elements from the wireframe document.

```html
<!DOCTYPE html>
<html lang="en">
<head>
<meta charset="utf-8">
<title>Orvane – Exam Prep Platform</title>
<link href="https://fonts.googleapis.com/css2?family=Open+Sans:wght@400;600;700&display=swap" rel="stylesheet">
<style>
:root{
  --bg:#ece8e0;
  --white:#ffffff;
  --ink:#3b3e48;
  --muted:#8a8d96;
  --dark:#363946;
  --dark-2:#575a68;
  --footer:#2f323d;
  --cyan:#12b3ea;
  --blue:#3d9cc3;
  --steel:#5b8fa8;
  --green:#a9cb38;
  --orange:#f28a22;
  --red:#e4502a;
  --pink:#d21f6b;
  --pale:#e1e5ec;
  --light:#f3f4f6;
}
*{box-sizing:border-box;margin:0;padding:0}
html,body{width:1043px;height:1200px;overflow:hidden;background:var(--bg);font-family:"Open Sans",Arial,sans-serif;color:var(--ink)}
.page{position:absolute;left:141px;top:0;width:760px;height:1200px;background:var(--white)}
.stripe{position:absolute;left:0;width:100%;height:4px;background:linear-gradient(90deg,var(--blue) 0 20%,var(--green) 20% 40%,var(--orange) 40% 60%,var(--red) 60% 80%,var(--pink) 80% 100%)}

/* header */
.site-header{position:absolute;top:0;left:0;width:100%;height:66px}
.brand{position:absolute;left:88px;top:17px;display:flex;align-items:center;gap:8px}
.brand-mark{width:22px;height:22px;background:var(--orange)}
.brand-name{font-weight:700;font-size:20px;color:var(--ink);letter-spacing:1px}
.brand-tag{position:absolute;left:30px;top:26px;font-size:7px;color:var(--muted);white-space:nowrap}
.main-nav{position:absolute;left:252px;top:25px;font-size:8px;color:var(--muted);letter-spacing:.3px}
.main-nav span{margin:0 3px}
.search{position:absolute;left:577px;top:20px;width:70px;height:16px;background:#f2f2f2;border-radius:2px;font-size:7px;color:#b5b5b5;padding:3px 6px}
.search svg{position:absolute;right:3px;top:2px}

/* hero */
.hero{position:absolute;top:66px;left:0;width:100%;height:296px;background:var(--dark);overflow:hidden}
.hero-light{position:absolute;inset:0}
.hero-title{position:absolute;left:212px;top:30px;color:var(--white);font-size:23px;font-weight:400}
.btn{position:absolute;left:502px;top:30px;width:119px;height:32px;background:var(--cyan);color:var(--white);font-size:11px;font-weight:600;display:flex;align-items:center;justify-content:center}
.arrow{position:absolute;top:118px}
.devices{position:absolute;left:210px;top:106px;width:335px;height:190px;background:linear-gradient(180deg,#f4f5f7,#d9dce2);border-radius:10px 10px 0 0}

/* features */
.features{position:absolute;top:362px;left:0;width:100%;height:263px;display:flex;justify-content:center;gap:10px;padding-top:50px}
.feature{width:188px;text-align:center}
.feature h3{font-size:15px;font-weight:400;color:var(--ink);white-space:nowrap}
.feature .icon{width:54px;height:54px;border-radius:50%;margin:12px auto 16px;display:flex;align-items:center;justify-content:center}
.feature p{font-size:8px;line-height:14px;color:#333}
.feature a{display:block;margin-top:11px;font-size:7.5px;font-weight:700;color:var(--cyan);text-decoration:none}

/* pain points */
.pain{position:absolute;top:625px;left:0;width:100%;height:293px;background:var(--pale)}
.pain h2{position:absolute;left:0;width:100%;top:34px;text-align:center;font-size:36px;font-weight:400;color:#555862}
.tile{position:absolute;width:113px;height:91px;display:flex;align-items:center;justify-content:center}
.label{position:absolute;font-size:20px;line-height:23px}

/* download & testimonial */
.extras{position:absolute;top:918px;left:0;width:100%;height:167px;background:var(--light)}
.extras h4{position:absolute;left:147px;top:16px;font-size:15px;font-weight:400}
.quote-title{position:absolute;left:537px;top:18px;font-size:10px}
.quote{position:absolute;left:546px;top:37px;width:85px;height:76px;border:1px solid var(--red);background:var(--white);padding:5px;font-size:5px;line-height:7px;color:#777}
.quote-by{position:absolute;left:568px;top:116px;font-size:5.5px;color:#555}
.quote-by b{color:var(--red)}

/* footer */
.site-footer{position:absolute;top:1089px;left:0;width:100%;height:111px;background:var(--footer);color:#d6d8de}
.foot-nav{position:absolute;left:108px;top:26px;font-size:8px}
.foot-nav span{margin:0 3px}
.copy{position:absolute;left:108px;top:49px;font-size:7.5px}
.legal{position:absolute;left:108px;top:75px;font-size:6.5px;line-height:13px}
.social{position:absolute;left:492px;top:25px;display:flex;gap:8px}
.social span{width:18px;height:18px;border-radius:2px;display:block}
</style>
</head>
<body>
<main class="page">

  <header class="site-header">
    <div class="brand">
      <span class="brand-mark"></span>
      <span class="brand-name">Orvane</span>
      <span class="brand-tag">Exam Prep Platform</span>
    </div>
    <nav class="main-nav">ABOUT<span>|</span>BLOG<span>|</span>JOBS<span>|</span>FAQ<span>|</span>FORUM<span>|</span>CONTACT US<span>|</span>TERM<span>|</span>PRIVACY</nav>
    <div class="search">Search
      <svg width="11" height="11" viewBox="0 0 11 11"><circle cx="4.5" cy="4.5" r="3.3" fill="none" stroke="#aaa" stroke-width="1.2"/><line x1="7" y1="7" x2="10" y2="10" stroke="#aaa" stroke-width="1.3"/></svg>
    </div>
    <div class="stripe" style="top:62px"></div>
  </header>

  <section class="hero">
    <svg class="hero-light" width="760" height="296"><polygon points="138,0 760,0 760,296 300,296" fill="var(--dark-2)"/></svg>
    <h1 class="hero-title">We made useful app!</h1>
    <div class="btn">Learn More</div>
    <svg class="arrow" style="left:82px" width="14" height="26"><polyline points="12,2 2,13 12,24" fill="none" stroke="#aeb1ba" stroke-width="2"/></svg>
    <svg class="arrow" style="left:664px" width="14" height="26"><polyline points="2,2 12,13 2,24" fill="none" stroke="#aeb1ba" stroke-width="2"/></svg>
    <div class="devices" role="img" aria-label="Laptop and phone showing the app store listing and the app's home screen"></div>
  </section>

  <section class="features">
    <article class="feature">
      <h3>How it's works</h3>
      <div class="icon" style="background:var(--steel)">
        <svg width="26" height="26" viewBox="0 0 26 26"><line x1="22" y1="4" x2="10" y2="16" stroke="#fff" stroke-width="3" stroke-linecap="round"/><circle cx="7" cy="19" r="4" fill="#fff"/></svg>
      </div>
      <p>Lorem ipsum dolor sit amet, consectetur adipiscing elit. Suspendisse rhoncus, lacus ac commodo volutpat, felis odio pulvinar enim, non dapibus mauris nulla sed ipsum.</p>
      <a href="#">READ MORE</a>
    </article>
    <article class="feature">
      <h3>Label Studying Method™</h3>
      <div class="icon" style="background:var(--green)">
        <svg width="26" height="26" viewBox="0 0 26 26"><line x1="18" y1="6" x2="7" y2="13" stroke="#fff" stroke-width="2"/><line x1="7" y1="13" x2="18" y2="20" stroke="#fff" stroke-width="2"/><circle cx="18" cy="6" r="3.5" fill="#fff"/><circle cx="7" cy="13" r="3.5" fill="#fff"/><circle cx="18" cy="20" r="3.5" fill="#fff"/></svg>
      </div>
      <p>It acts like an X-ray for the KVEX questions. By learning to identify the concepts that are being tested, you will be able to find the right answer faster.</p>
      <a href="#">READ MORE</a>
    </article>
    <article class="feature">
      <h3>Study On the move</h3>
      <div class="icon" style="background:var(--orange)">
        <svg width="20" height="30" viewBox="0 0 20 30"><rect x="2" y="1" width="16" height="28" rx="3" fill="none" stroke="#fff" stroke-width="2"/><rect x="5" y="5" width="10" height="17" fill="#fff"/></svg>
      </div>
      <p>The Tutorbrix mobile app works offline, so lets you study for the KVEX whenever and wherever you want. Whether you are on a plane or in a train or have some time to spare during your break.</p>
      <a href="#">READ MORE</a>
    </article>
  </section>

  <section class="pain">
    <h2>Why existing tools are a pain</h2>
    <div class="tile" style="left:167px;top:103px;background:var(--green)">
      <svg width="50" height="52" viewBox="0 0 50 52"><path d="M12 4h22v24l-9 22c-4 0-6-3-5-7l2-10H8c-3 0-5-3-4-6l4-19c1-3 2-4 4-4z" fill="#fff"/><rect x="36" y="4" width="9" height="24" fill="#fff"/></svg>
    </div>
    <span class="label" style="left:158px;top:200px;color:var(--green)">Ineffective</span>
    <div class="tile" style="left:394px;top:103px;background:var(--orange)">
      <svg width="60" height="46" viewBox="0 0 60 46"><path d="M14 6l26-5 3 10" fill="#fff"/><rect x="6" y="10" width="48" height="34" rx="3" fill="#fff"/><rect x="40" y="22" width="16" height="10" rx="2" fill="var(--orange)"/><circle cx="46" cy="27" r="2" fill="#fff"/></svg>
    </div>
    <span class="label" style="left:374px;top:195px;color:var(--orange);transform:rotate(-90deg);transform-origin:0 0">Expensive</span>
    <span class="label" style="left:518px;top:107px;color:var(--pink)">No serious<br>mobile<br>solution</span>
    <div class="tile" style="left:281px;top:194px;background:var(--red)">
      <svg width="60" height="54" viewBox="0 0 60 54"><rect x="4" y="34" width="13" height="20" fill="#fff"/><rect x="22" y="18" width="13" height="36" fill="#fff"/><rect x="40" y="2" width="13" height="52" fill="#fff"/></svg>
    </div>
    <span class="label" style="left:396px;top:197px;color:var(--red)">No detailed &amp;<br>actionable<br>analytics</span>
    <div class="tile" style="left:508px;top:194px;background:var(--pink)">
      <svg width="32" height="60" viewBox="0 0 32 60"><rect x="2" y="1" width="28" height="58" rx="5" fill="#fff"/><rect x="6" y="9" width="20" height="36" fill="var(--pink)"/><circle cx="16" cy="52" r="3" fill="var(--pink)"/></svg>
    </div>
  </section>

  <section class="extras">
    <h4>Download NOW!</h4>
    <svg style="position:absolute;left:162px;top:44px" width="92" height="76" viewBox="0 0 92 76">
      <rect x="2" y="18" width="26" height="54" rx="3" fill="#2f323d"/><rect x="5" y="25" width="20" height="38" fill="#8d9098"/>
      <rect x="34" y="2" width="56" height="74" rx="3" fill="#2f323d"/><rect x="38" y="8" width="48" height="62" fill="#8d9098"/>
    </svg>
    <span class="quote-title">What Customers Say</span>
    <div class="quote">Finally a study tool that fits my commute. The drills are short, clear and the progress charts keep me honest every single week.</div>
    <span class="quote-by"><b>Mira Tolen</b>, Manager</span>
  </section>

  <div class="stripe" style="top:1085px"></div>
  <footer class="site-footer">
    <nav class="foot-nav">ABOUT<span>|</span>BLOG<span>|</span>JOBS<span>|</span>FAQ<span>|</span>FORUM<span>|</span>CONTACT US<span>|</span>TERM<span>|</span>PRIVACY</nav>
    <p class="copy">© 2013 Orvane. All Rights Reserved.</p>
    <p class="legal">The logos used in the design are the property of their respective owners / copyright holders.</p>
    <div class="social">
      <span style="background:#3b5998"></span>
      <span style="background:#0e76a8"></span>
      <span style="background:#1da1f2"></span>
      <span style="background:#cb2027"></span>
      <span style="background:#ea4c89"></span>
      <span style="background:#dd4b39"></span>
    </div>
  </footer>

</main>
</body>
</html>
```